Business Card Redesign

We are looking for a designer to redesign our current business card (attached below). The logo itself will not change but the look and feel of the rest of the card needs to be freshened up. The text on the back of the card is to be changed to:
Strategic Alignment
Leadership and Coaching
Sales Force Development
Sales Talent Acquisition
Emotional Intelligence Facilitation & Certification
Guest speaking

The byline needs to be retained "Genuine connections... confident growth" along with the logo.

All up we will need business cards laid out for 6 people.

Also, once we receive a design that we are happy with we will need the branding to be continued through onto other documentation such as workbook cover pages, email signatures etc and will negotiate with the successful designer on this future piece of work.

Please review our website for more of an idea of who we are, our style, and what we do. www.brightharbourgroup.com.au and www.heartwiseskills-qm-z.com.au.

Thank you for your interest.

```html
<!DOCTYPE html>
<html lang="en">
<head>
<meta charset="utf-8">
<title>Bright Harbour Consulting – Business Cards</title>
<link rel="stylesheet" href="https://fonts.googleapis.com/css2?family=Mulish:wght@400;600;800&display=swap">
<style>
  :root {
    --bg: #2a2a2c;
    --card-white: #ffffff;
    --card-shade: #eef1f4;
    --navy: #0c4778;
    --navy-deep: #083a63;
    --sky: #1e93cf;
    --sky-soft: #5fb6e2;
    --grey-text: #6b6f74;
    --light-text: #dfe9f2;
  }
  * { margin: 0; padding: 0; box-sizing: border-box; }
  html, body { width: 1200px; height: 900px; overflow: hidden; }
  body {
    background: var(--bg);
    font-family: "Mulish", sans-serif;
    position: relative;
  }
  .card {
    position: absolute;
    top: 288px;
    width: 540px;
    height: 324px;
    border-radius: 18px;
    overflow: hidden;
    background: linear-gradient(160deg, var(--card-white) 40%, var(--card-shade) 100%);
  }
  .card-back { left: 30px; }
  .card-front { left: 630px; background: var(--card-white); }

  /* Brand wordmark */
  .brand {
    display: flex;
    align-items: center;
    gap: 12px;
    color: var(--navy);
    font-weight: 800;
    letter-spacing: -0.5px;
  }
  .brand-dot {
    width: 34px; height: 34px;
    border-radius: 50%;
    background: var(--sky);
    flex: none;
  }

  /* Back card */
  .card-back .brand { position: absolute; left: 50px; top: 92px; font-size: 31px; }
  .back-rule {
    position: absolute; left: 50px; top: 150px;
    width: 440px; height: 1px; background: var(--sky-soft);
  }
  .services {
    position: absolute; left: 50px; top: 166px; width: 440px;
    list-style: none;
    color: var(--grey-text);
    font-size: 13px;
    line-height: 22px;
  }

  /* Front card */
  .front-band { position: absolute; inset: 0; }
  .card-front .brand { position: absolute; left: 28px; top: 34px; font-size: 28px; }
  .tagline {
    position: absolute; left: 74px; top: 80px;
    color: var(--grey-text);
    font-size: 13px; font-weight: 600;
  }
  .person {
    position: absolute; left: 30px; top: 210px;
    color: var(--light-text);
  }
  .person-name { color: #fff; font-size: 19px; font-weight: 800; }
  .person-role { font-size: 13px; margin: 2px 0 10px; }
  .contact-line { font-size: 13px; line-height: 20px; }
  .contact-line b { color: var(--sky-soft); font-weight: 800; margin-right: 6px; }
  .office {
    position: absolute; right: 28px; top: 196px;
    text-align: right;
    font-style: normal;
    color: var(--light-text);
    font-size: 13px; line-height: 20px;
  }
  .office-web { color: var(--sky-soft); font-weight: 800; }
</style>
</head>
<body>

  <section class="card card-back" aria-label="Card back">
    <div class="brand"><span class="brand-dot"></span>Bright Harbour Consulting</div>
    <div class="back-rule"></div>
    <ul class="services">
      <li>Strategic Alignment • Leadership and Coaching</li>
      <li>Sales Force Development • Sales Talent Acquisition</li>
      <li>Emotional Intelligence Facilitation &amp; Certification • Guest speaking</li>
    </ul>
  </section>

  <section class="card card-front" aria-label="Card front">
    <svg class="front-band" width="540" height="324" viewBox="0 0 540 324" aria-hidden="true">
      <path d="M0,160 Q300,150 540,46 L540,60 Q300,164 0,172 Z" fill="var(--sky)"/>
      <path d="M0,176 Q300,168 540,66 L540,324 L0,324 Z" fill="var(--navy)"/>
      <path d="M170,150 Q380,125 540,74 L540,92 Q380,140 170,150 Z" fill="var(--navy-deep)"/>
      <path d="M0,176 Q300,168 540,66 L540,72 Q300,174 0,182 Z" fill="var(--sky-soft)" opacity="0.6"/>
    </svg>

    <div class="brand"><span class="brand-dot"></span>Bright Harbour Consulting</div>
    <p class="tagline">Genuine connections... confident growth</p>

    <div class="person">
      <p class="person-name">Daniel Marlowe</p>
      <p class="person-role">Managing Director</p>
      <p class="contact-line"><b>m:</b>+613 9555 0142</p>
      <p class="contact-line"><b>e :</b>daniel@brightharbourgroup.com.au</p>
    </div>

    <address class="office">
      Suite 4.08, 210 Harbour Rd<br>
      Southbank Australia 3006<br>
      <span class="office-web">www.brightharbourgroup.com.au</span>
    </address>
  </section>

</body>
</html>
```